Flyer Design für Kosmetikerin und Visagistin gesucht
Zielgruppe
Ich bin ein Einmannbetrieb und biete Kosmetik für Frauen, Männer und Jugendliche, Visagistik, Nageldesign und Wimpernverlängerun an - eine bestimmte Zielgruppe gibt es eigentlich nicht - es sollen alle angesprochen werden.
Aufgabenstellung
Ich hätte gerne einen Flyer, welcher beidseitig bedruckt wird und welchen ich dann per Postwurfsendung an die Haushalte in meiner Umgebung verteilen kann, da ich gerade mein Kosmetikstudio eröffnet habe. Auf der Vorderseite hätte ich gerne meinen Namen, Dipl. Kosmetikerin, Dipl. Make-up-Artist, Dipl. Nageldesignerin, meine Adresse (eventuell kleine Karte) und meine Telefonnummer mit dem Hinweis 'Termine nach telefonischer Vereinbarung' Und meine Mailadresse.
Weiters hätte ich gerne 'Neueröffnung', 'tolle Eröffnungsangbote bis Jahresende', 'kleines Willkommensgeschenk solange der Vorrat reicht' und den Satz 'der erste Eindruck hat keine zweite Chance' darauf. Ansonsten gilt bei der Vorderseite freie Gestaltung!
Auf der Rückseite hätte ich gerne meine Preisliste - ich lade sie mal als PDF-Datei hoch...
Ich lade auch mein Logo, meine Preisliste und ein paar Bilder hoch, die Bilder dürfen verwendet werden, denn ich habe dafür auch bezahlt - ist aber keine Pflicht - bin für jede andere Idee offen! Bevorzugten Farben sind Rosa und Pink, es darf auch versielt sein! Das Format, ob quer, hochgestellt, gefaltet usw. ist mir eigentlich egal - die Preisliste soll nur gut leserlich sein - kann auch von der Anordnung her verändert werden.

```html
<!DOCTYPE html>
<html lang="de">
<head>
<meta charset="utf-8">
<title>Rosé Atelier – Faltblatt</title>
<link href="https://fonts.googleapis.com/css2?family=Fira+Sans:wght@400&family=Abel&family=Oswald:wght@500;600&display=swap" rel="stylesheet">
<style>
:root{
  --pink:#c4157f;
  --pink-soft:#d9559f;
  --rose:#f4dbe8;
  --rose-pale:#fbeef5;
  --ink:#1c1c1c;
  --paper:#ffffff;
  --shadow:rgba(0,0,0,.28);
}
*{margin:0;padding:0;box-sizing:border-box}
html,body{width:1200px;height:848px;overflow:hidden;background:var(--paper)}
body{position:relative;font-family:"Abel",sans-serif;color:var(--ink)}

.board-label{position:absolute;font-family:"Fira Sans",sans-serif;font-size:23px;color:var(--ink);white-space:nowrap}
.label-front{left:134px;top:62px;transform:rotate(-4deg)}
.label-back{left:451px;top:145px;transform:translateX(-50%)}
.label-inside{left:885px;top:145px;transform:translateX(-50%)}

.panel{position:absolute;background:var(--paper);box-shadow:1px 2px 5px var(--shadow);overflow:hidden}

/* Vorderseite */
.front{left:102px;top:96px;width:237px;height:508px;transform:rotate(-5.6deg)}
.front-photo{position:absolute;left:0;top:0;width:100%;height:312px;
  background:linear-gradient(160deg,#3a2a24 0%,#7a5646 30%,#e9c2b0 55%,#d7a793 75%,#6d4a3c 100%)}
.front-quote{position:absolute;left:12px;top:16px;font-family:"Oswald",sans-serif;font-weight:600;font-size:15px;line-height:17px;color:#fff;text-transform:uppercase;letter-spacing:.2px}
.front-opening{position:absolute;left:10px;top:272px;font-family:"Oswald",sans-serif;font-weight:600;font-size:19px;color:#fff;letter-spacing:.3px}
.front-badge{position:absolute;left:168px;top:242px;width:62px;height:62px;border-radius:50%;background:var(--pink);color:#fff;font-family:"Oswald",sans-serif;font-weight:500;font-size:8.2px;line-height:9.5px;display:flex;align-items:center;justify-content:center;text-align:center;transform:rotate(-8deg)}
.front-tiles{position:absolute;left:0;top:312px;width:100%;height:88px;display:flex}
.front-tile{flex:1}
.tile-facial{background:linear-gradient(135deg,#d8d2cc,#f1ece8 60%,#a89a90)}
.tile-orchid{background:linear-gradient(135deg,#b25fb4,#e7c7e6 55%,#5d3c4b)}
.tile-nails{background:linear-gradient(135deg,#f3dcd2,#e8b8c4 50%,#b98ad0)}
.front-gift{position:absolute;left:84px;top:408px;width:148px;font-size:8.8px;line-height:10px;color:var(--ink)}
.front-brand{position:absolute;left:18px;top:440px;width:206px;text-align:center}
.brand-name{font-family:"Abel",sans-serif;font-size:25px;color:var(--pink-soft);line-height:28px}
.brand-line{font-size:4.6px;letter-spacing:.3px;color:#fff;background:var(--pink-soft);display:inline-block;padding:1px 4px;margin-top:2px;white-space:nowrap}

/* Rückseite */
.back{left:331px;top:180px;width:239px;height:506px}
.back-map{position:absolute;left:10px;top:12px;width:218px;height:151px;background:var(--rose-pale);border:1px solid var(--rose)}
.back-brand{position:absolute;left:0;top:222px;width:100%;text-align:center}
.back-brand .brand-name{font-size:22px;line-height:24px}
.back-info{position:absolute;left:0;top:277px;width:100%;text-align:center;font-size:7.2px;line-height:9.6px}
.info-head{color:var(--pink);font-weight:bold;letter-spacing:.2px}
.info-owner{font-weight:bold}
.gap{height:9.6px}
.back-appointment{position:absolute;left:51px;top:413px;width:138px;height:77px;background:var(--rose-pale);border:1px solid #e7a9c9;font-size:7.2px;text-align:center;padding-top:62px}

/* Innenseiten */
.inside{left:646px;top:180px;width:477px;height:506px}
.price-title{position:absolute;left:12px;top:11px;font-family:"Abel",sans-serif;font-weight:bold;font-size:12.5px;line-height:14px;color:var(--pink)}
.price-col{position:absolute;font-size:6.3px;line-height:9.2px}
.price-col > div{line-height:9.2px}
.col-left{left:12px;top:64px;width:226px}
.col-right{left:248px;top:12px;width:219px}
.cat{color:var(--pink-soft)}
.row{display:flex;align-items:flex-end}
.row .item{flex:1;white-space:nowrap;overflow:hidden}
.row .price{width:34px;white-space:nowrap;display:flex;justify-content:space-between;line-height:9.2px}
.inside-photo{position:absolute;left:0;bottom:0;width:100%;height:66px;
  background:linear-gradient(180deg,rgba(255,255,255,1) 0%,rgba(240,214,200,.9) 45%,#e3b9a4 100%)}

.spec{position:absolute;left:645px;top:710px;font-family:"Fira Sans",sans-serif;font-size:22.5px;line-height:27.5px;color:var(--ink)}
</style>
</head>
<body>

<div class="board-label label-front">Vorderseite</div>
<div class="board-label label-back">Rückseite</div>
<div class="board-label label-inside">Innenseiten</div>

<!-- Vorderseite -->
<section class="panel front">
  <div class="front-photo" role="img" aria-label="Porträtfoto einer Frau mit geschlossenen Augen, fliederfarbenem Lidschatten und pinkem Lippenstift"></div>
  <p class="front-quote">„Der erste Eindruck hat<br>keine zweite Chance“</p>
  <p class="front-opening">NEUERÖFFNUNG</p>
  <div class="front-badge">Tolle<br>Eröffnungs-<br>angebote bis<br>Jahresende</div>
  <div class="front-tiles">
    <div class="front-tile tile-facial" role="img" aria-label="Foto einer Gesichtsmaske, die mit Pinsel aufgetragen wird"></div>
    <div class="front-tile tile-orchid" role="img" aria-label="Foto einer lila Orchidee mit Make-up-Pinseln"></div>
    <div class="front-tile tile-nails" role="img" aria-label="Foto gepflegter Fingernägel mit Schmucksteinen"></div>
  </div>
  <p class="front-gift">Und ein kleines Willkommens-<br>geschenk solange der Vorrat reicht!</p>
  <div class="front-brand">
    <div class="brand-name">Rosé Atelier</div>
    <div class="brand-line">KOSMETIK | VISAGISTIK | NAGELDESIGN | WIMPERNVERLÄNGERUNG</div>
  </div>
</section>

<!-- Rückseite -->
<section class="panel back">
  <div class="back-map" role="img" aria-label="Lageplan mit Straßen und Standort des Studios"></div>
  <div class="back-brand">
    <div class="brand-name">Rosé Atelier</div>
    <div class="brand-line">KOSMETIK | VISAGISTIK | NAGELDESIGN | WIMPERNVERLÄNGERUNG</div>
  </div>
  <div class="back-info">
    <div class="info-head">INHABERIN:</div>
    <div class="info-owner">Marion Hollweg</div>
    <div>Dipl. Kosmetikerin</div>
    <div>Dipl. Make-up-Artist</div>
    <div>Dipl. Nageldesignerin</div>
    <div class="gap"></div>
    <div>Lindengasse 12</div>
    <div>2301 Wiesenau</div>
    <div>Telefon: 0660.4821937</div>
    <div>E-Mail: hallo@roseatelier.at</div>
    <div class="gap"></div>
    <div class="info-head">ÖFFNUNGSZEITEN:</div>
    <div>Termine nach telefonischer Vereinbarung</div>
  </div>
  <div class="back-appointment">Ihr nächster Termin</div>
</section>

<!-- Innenseiten -->
<section class="panel inside">
  <h1 class="price-title">Preisliste 2013</h1>

  <div class="price-col col-left">
    <div class="cat">Gesichtsbehandlung für Eilige</div>
    <div class="row"><span class="item">Reinigung, Hautanalyse, Tonic, Peeling, Maske, Tagespflege</span><span class="price"><span>€</span><span>25,00</span></span></div>
    <div class="cat">Gesichtsbehandlung klassisch</div>
    <div class="row"><span class="item">Reinigung, Hautanalyse, Peeling, Dampf, Ausreinigen, Tonic,<br>Maske, Lippenpflege, Massage, Augen- u.Tagespflege</span><span class="price"><span>€</span><span>38,00</span></span></div>
    <div class="cat">Gesichtsbehandlung deluxe</div>
    <div class="row"><span class="item">Reinigung, Hautanalyse, Peeling, Wimpern od. Augenbrauen<br>färben, Dampf, Ausreinigen, Tonic, Augenbrauen faconieren,<br>Ampulle, Maske, Lippenpflege, Massage, Augen- und Tages-<br>pflege</span><span class="price"><span>€</span><span>52,00</span></span></div>
    <div class="cat">Gesichtsbehandlung Anti-Age spezial</div>
    <div class="row"><span class="item">Reinigung, Hautanalyse, Peeling, Dampf, Ausreinigen, Tonic,<br>Ampulle bzw. Serum, Anti-Aging-Spezialmaske od.<br>Collagen-Vlies nach Hauttyp, Lippenpflege, Augenampulle,<br>Massage, Augen- und Antiaging-Tagespflege</span><span class="price"><span>€</span><span>76,00</span></span></div>
    <div class="cat">Microdermabrasionbehandlung</div>
    <div class="row"><span class="item">Reinigung, Peeling, Microdermabrasion, Ampulle od. Serum,<br>Maske, Augen- u. Tagespflege</span><span class="price"><span>€</span><span>54,00</span></span></div>
    <div class="row"><span class="item">Microdermabrasion-Kur 4x mit Wochenabstand</span><span class="price"><span>€</span><span>205,00</span></span></div>
    <div class="cat">Fruchtsäurebehandlung</div>
    <div class="row"><span class="item">Reinigung, Peeling, AHA-Fruchtsäuretonic, AHA-Gingko-<br>somengel, Milchsäurevlies, Massage mit Vit.C-Creme,<br>Augen- u. Tagespflege</span><span class="price"><span>€</span><span>58,00</span></span></div>
    <div class="row"><span class="item">Kur 4x mit Wochenabstand</span><span class="price"><span>€</span><span>220,00</span></span></div>
    <div class="cat">Microdermabrasion mit Fruchtsäure kombiniert</div>
    <div class="row"><span class="item">Reinigung, Peeling, Microdermabrasion, AHA-Fruchtsäure-<br>tonic, AHA-Gingkosomengel, Milchsäure-Vlies, Massage<br>mit Vit.C-Creme, Augen- und Tagespflege</span><span class="price"><span>€</span><span>105,00</span></span></div>
    <div class="row"><span class="item">Kur 4x mit Wochenabstand</span><span class="price"><span>€</span><span>410,00</span></span></div>
    <div class="cat">Aknespezialbehandlung</div>
    <div class="row"><span class="item">Reinigung, Peeling, Dampf, Ausreinigen, Tonic, Ampulle,<br>Aknespezialmaske, Spezialtagespflege</span><span class="price"><span>€</span><span>38,00</span></span></div>
    <div class="cat">Pigmentfleckenspezialbehandlung</div>
    <div class="row"><span class="item">Reinigung, Peeling, Dampf, Spezialserum, Spezialmaske<br>gegen Pigmentflecken, Augenpflege, Spezialtagespflege</span><span class="price"><span>€</span><span>48,00</span></span></div>
    <div class="cat">Anticouperosespezialbehandlung</div>
    <div class="row"><span class="item">Reinigung, Peeling, Dampf, Spezialserum, Spezialmaske,<br>Augenpflege, Spezialtagespflege</span><span class="price"><span>€</span><span>48,00</span></span></div>
    <div class="row"><span class="item">Gesicht-, Hals- und Dekolletemassage (ca 20 min)</span><span class="price"><span>€</span><span>18,00</span></span></div>
    <div class="row"><span class="item">Kosmetische Lymphdrainage (ca. 30 min)</span><span class="price"><span>€</span><span>23,00</span></span></div>
  </div>

  <div class="price-col col-right">
    <div class="cat">Zusatzbehandlungen:</div>
    <div class="row"><span class="item">Wimpern färben</span><span class="price"><span>€</span><span>6,00</span></span></div>
    <div class="row"><span class="item">Augenbrauen färben</span><span class="price"><span>€</span><span>5,00</span></span></div>
    <div class="row"><span class="item">Augenbrauen faconnieren/harzen</span><span class="price"><span>€</span><span>4,00</span></span></div>
    <div class="row"><span class="item">Augen-Intensivbehandlung</span><span class="price"><span>€</span><span>18,00</span></span></div>
    <div class="row"><span class="item">Wimperndauerwelle</span><span class="price"><span>€</span><span>18,00</span></span></div>
    <div class="row"><span class="item">Kinn harzen</span><span class="price"><span>€</span><span>6,00</span></span></div>
    <div class="row"><span class="item">Oberlippe harzen</span><span class="price"><span>€</span><span>4,00</span></span></div>
    <div class="row"><span class="item">Wirkstoffampulle</span><span class="price"><span>€</span><span>8,00</span></span></div>
    <div class="row"><span class="item">Hochfrequenz</span><span class="price"><span>€</span><span>6,00</span></span></div>
    <div class="row"><span class="item cat">Cellulite-/Entschlackungswickel</span><span class="price"><span>€</span><span>32,00</span></span></div>
    <div class="row"><span class="item">10er Block: 10 + 1 gratis</span><span class="price"><span>€</span><span>320,00</span></span></div>
    <div class="cat">Hände:</div>
    <div class="row"><span class="item">Klassische Maniküre mit Pflege oder Farb-Lack</span><span class="price"><span>€</span><span>16,00</span></span></div>
    <div class="row"><span class="item">Maniküre mit Handpeeling und Paraffinbad</span><span class="price"><span>€</span><span>32,00</span></span></div>
    <div class="row"><span class="item">Handpeeling + Paraffinbad</span><span class="price"><span>€</span><span>18,00</span></span></div>
    <div class="row"><span class="item">Permanenter Gel-Lack am Naturnagel</span><span class="price"><span>€</span><span>16,00</span></span></div>
    <div class="row"><span class="item">French</span><span class="price"><span>€</span><span>2,00</span></span></div>
    <div class="row"><span class="item">Gellack entfernen mit Pflege</span><span class="price"><span>€</span><span>12,00</span></span></div>
    <div class="row"><span class="item">Nagelmodellage mit Gel</span><span class="price"></span></div>
    <div class="row"><span class="item">Neues Set</span><span class="price"><span>€</span><span>48,00</span></span></div>
    <div class="row"><span class="item">Auffüllen All inclusive (French, Fullcover, Glitzer, Nailart/<br>Steinchen/Airbrush/Sticker auf 2 Finger)</span><span class="price"><span>€</span><span>38,00</span></span></div>
    <div class="row"><span class="item">Nailart/Steinchen/Airbrush/Sticker zusätzlich pro Finger</span><span class="price"><span>€</span><span>0,50</span></span></div>
    <div class="row"><span class="item">Modellage entfernen mit Pflege</span><span class="price"><span>€</span><span>16,00</span></span></div>
    <div class="cat">Permanente Wimpernverlängerung</div>
    <div class="row"><span class="item">erstes Set</span><span class="price"><span>€</span><span>115,00</span></span></div>
    <div class="row"><span class="item">Auffüllen innerhalb von 3 Wochen</span><span class="price"><span>€</span><span>40,00</span></span></div>
    <div class="row"><span class="item">Innerhalb von 4-5 Wochen</span><span class="price"><span>€</span><span>50,00</span></span></div>
    <div class="cat">Enthaarung:</div>
    <div class="row"><span class="item">Beine harzen inkl. Knie</span><span class="price"><span>€</span><span>18,00</span></span></div>
    <div class="row"><span class="item">Beine komplett harzen</span><span class="price"><span>€</span><span>28,00</span></span></div>
    <div class="row"><span class="item">Achseln harzen</span><span class="price"><span>€</span><span>11,00</span></span></div>
    <div class="row"><span class="item">Bikinizone harzen</span><span class="price"><span>€</span><span>12,00</span></span></div>
    <div class="row"><span class="item">Arme harzen</span><span class="price"><span>€</span><span>22,00</span></span></div>
    <div class="row"><span class="item">Harzpackage klein (Beine inkl. Knie, Achseln, Bikinizone)</span><span class="price"><span>€</span><span>38,00</span></span></div>
    <div class="row"><span class="item">Harzpackage groß (Beine, Achseln, Bikinizone, Arme)</span><span class="price"><span>€</span><span>68,00</span></span></div>
    <div class="row"><span class="item">Männer: Rücken harzen</span><span class="price"><span>€</span><span>26,00</span></span></div>
    <div class="row"><span class="item">Brust u. Bauch harzen</span><span class="price"><span>€</span><span>26,00</span></span></div>
    <div class="cat">Make up:</div>
    <div class="row"><span class="item">Dezentes Tagesmake up</span><span class="price"><span>€</span><span>22,00</span></span></div>
    <div class="row"><span class="item">Abendmake up</span><span class="price"><span>€</span><span>26,00</span></span></div>
    <div class="row"><span class="item">Hochzeitsmake up inkl. 1 Probetermin</span><span class="price"><span>€</span><span>48,00</span></span></div>
    <div class="row"><span class="item">Brautpackage (Probe-Make up, Make up am Tag<br>der Hochzeit, Nagelmodellage, Wimpernverlängerung)</span><span class="price"><span>€</span><span>199,00</span></span></div>
  </div>

  <div class="inside-photo" role="img" aria-label="Foto eines liegenden Frauenprofils bei einer entspannenden Gesichtsbehandlung"></div>
</section>

<div class="spec">
  Faltblatt | Einbruchfalz<br>
  DIN lang | Hochformat<br>
  4seitig<br>
  4/4-farbig
</div>

</body>
</html>
```